Business Card Design

I'm a Naturopathic Physician specializing in the treatment of autoimmune disorders, supportive cancer care and stress, anxiety and depressive disorders.

I practice out of 3 clinic locations and I want a business card design which can be easily changed to include 3 clinic locations, addresses, and contact info.

My website is VeltarisHealth.com and this will promote me personally as a specialist in these treatment areas. I would like one side of the business card to promote this site with the tag line "Specializing in Immune and Related Disorders"

REVIEW THE DESCRIPTION AND UPLOADS FOR MY DESIGN STYLE PREFERENCES.

Industry/Entity Type

Clinic

Colors
9bcb3c
fbed22
0455a3

Requirements
Must have
• Would prefer a vertical design.
Would like bold, simple colors and contrasts

Please visit http://plovexa.com/veltarishealth/ for some color and design "feel"

Do not feel the Designs HAVE to have the logo in it... I want SIMPLE, CLEAN and BOLD design so if the Logo makes the designs too busy, please omit

Dr. Marcus Fenholt BSc ND
Naturopathic Physician

"Clinic Name"
"Clinic Address"
"Clinic Tel"
"Clinic E-Mail"
"Clinic Website"

Please review the PDF for design styles I prefer.

Please Note: Once I determine if there are design concepts worthy of going forward with, I will forward specific contact and clinic information at that time for final design

```html
<!DOCTYPE html>
<html lang="en">
<head>
<meta charset="utf-8">
<title>VeltarisHealth – Business Card</title>
<link href="https://fonts.googleapis.com/css2?family=Open+Sans:wght@400;600;700&display=swap" rel="stylesheet">
<style>
  :root {
    --green: #9bcb3c;
    --blue: #0f4f96;
    --blue-text: #0c4a93;
    --white: #ffffff;
    --paper: #f8f8f6;
    --backdrop: #e9e6e1;
  }
  * { margin: 0; padding: 0; box-sizing: border-box; }
  html, body { width: 1108px; height: 1200px; overflow: hidden; }
  body {
    background: var(--backdrop);
    font-family: "Open Sans", Arial, sans-serif;
    position: relative;
  }
  .card {
    position: absolute;
    top: 210px;
    width: 480px;
    height: 780px;
    overflow: hidden;
    box-shadow: 0 6px 18px rgba(0,0,0,0.18);
  }
  .card--front { left: 50px; background: var(--green); color: var(--white); }
  .card--back { left: 578px; background: var(--paper); }

  .brand { font-weight: 700; letter-spacing: 0.5px; }

  .card--front .brand { position: absolute; top: 250px; left: 60px; font-size: 40px; color: var(--white); }

  .services { position: absolute; top: 330px; left: 60px; list-style: none; font-size: 22px; line-height: 32px; }
  .services li { position: relative; padding-left: 24px; }
  .services li::before {
    content: ""; position: absolute; left: 0; top: 13px;
    width: 8px; height: 8px; border-radius: 50%; background: var(--white);
  }
  .site { position: absolute; left: 0; right: 0; bottom: 80px; text-align: center; font-size: 24px; }

  .card--back .brand { position: absolute; top: 80px; left: 0; right: 0; text-align: center; font-size: 38px; color: var(--green); }
  .tagline {
    position: absolute; top: 150px; left: 0; right: 0; text-align: center;
    color: var(--blue-text); font-size: 22px; line-height: 32px;
  }
  .wave { position: absolute; left: 0; top: 230px; width: 480px; height: 550px; }

  .contact { position: absolute; top: 380px; left: 40px; right: 30px; color: var(--white); }
  .contact__name { font-size: 27px; font-weight: 600; }
  .contact__role { font-size: 21px; margin-top: 4px; }
  .contact__row { display: flex; align-items: flex-start; gap: 14px; font-size: 21px; line-height: 27px; }
  .contact__row svg { width: 22px; height: 22px; flex: none; margin-top: 3px; }
  .contact__address { margin-top: 44px; }
  .contact__lines { margin-top: 26px; display: flex; flex-direction: column; gap: 4px; }
</style>
</head>
<body>

<section class="card card--front">
  <p class="brand">VeltarisHealth</p>
  <ul class="services">
    <li>Autoimmune Disease</li>
    <li>Cancer Support &amp; Treatment</li>
    <li>Digestive Disorders</li>
    <li>Chronic Pain &amp; Inflammation</li>
    <li>Stress, Anxiety &amp; Depression</li>
    <li>Chronic Fatigue Disorders</li>
    <li>Hormonal Balancing</li>
    <li>General Health &amp; Wellness</li>
  </ul>
  <p class="site">www.VeltarisHealth.com</p>
</section>

<section class="card card--back">
  <p class="brand">VeltarisHealth</p>
  <p class="tagline">Specializing in Immune<br>System &amp; Related Disorders</p>

  <svg class="wave" viewBox="0 0 480 550" preserveAspectRatio="none" aria-hidden="true">
    <path d="M0 25 C 90 70, 170 95, 260 60 C 340 30, 410 10, 480 40 L480 550 L0 550 Z" fill="#9bcb3c"/>
    <path d="M0 38 C 90 85, 170 110, 260 75 C 340 45, 410 22, 480 50 L480 550 L0 550 Z" fill="#0f4f96"/>
  </svg>

  <div class="contact">
    <p class="contact__name">Dr. Marcus Fenholt BSc ND</p>
    <p class="contact__role">Naturopathic Physician</p>

    <div class="contact__row contact__address">
      <svg viewBox="0 0 24 24" aria-hidden="true"><circle cx="12" cy="12" r="11" fill="#9bcb3c"/><path d="M12 5a4.5 4.5 0 0 0-4.5 4.5C7.5 13 12 18.5 12 18.5s4.5-5.5 4.5-9A4.5 4.5 0 0 0 12 5z" fill="#0f4f96"/><circle cx="12" cy="9.5" r="1.7" fill="#9bcb3c"/></svg>
      <p>Brightleaf Market<br>2270 Larkmoor Road,<br>Halden, N.S<br>B3X 4K7</p>
    </div>

    <div class="contact__lines">
      <div class="contact__row">
        <svg viewBox="0 0 24 24" aria-hidden="true"><circle cx="12" cy="12" r="11" fill="#9bcb3c"/><path d="M8.5 6.5l2 2.5-1.2 1.4a8 8 0 0 0 4.3 4.3l1.4-1.2 2.5 2-1.3 1.8C11 17 7 13 6.7 7.8z" fill="#0f4f96"/></svg>
        <p>902.555.0147</p>
      </div>
      <div class="contact__row">
        <svg viewBox="0 0 24 24" aria-hidden="true"><circle cx="12" cy="12" r="11" fill="#9bcb3c"/><rect x="8.5" y="5.5" width="7" height="4" fill="#0f4f96"/><rect x="6" y="10" width="12" height="5.5" rx="1" fill="#0f4f96"/><rect x="8.5" y="13.5" width="7" height="4.5" fill="#0f4f96" stroke="#9bcb3c" stroke-width="1"/></svg>
        <p>902.555.0193</p>
      </div>
      <div class="contact__row">
        <svg viewBox="0 0 24 24" aria-hidden="true"><circle cx="12" cy="12" r="11" fill="#9bcb3c"/><rect x="6" y="8" width="12" height="8.5" rx="1" fill="#0f4f96"/><path d="M6.5 8.5l5.5 4.3 5.5-4.3" fill="none" stroke="#9bcb3c" stroke-width="1.3"/></svg>
        <p>care@veltarishealth.ca</p>
      </div>
    </div>
  </div>
</section>

</body>
</html>
```